Packaging design for a revolutionary hi-protein snack of Norwegian salmon

We need a breathtaking packing design for a smal snack bag (30 g) for a revolutionary new hi-protein snack made of Norwegian salmon. The product will be made with two different flavors; MANGO and WASABI. The product is extreme high in protein (60%) and omega 3, and are just natural.

We want to see a bold and fresh design that appeals to protein lovers of all ages.

Target Market(s)

Our target market is boys and girls that are 18-35 years old and that are interested in working out and eating healthy.

Industry/Entity Type

Snack industry (functional food, healthy snack, protein snack)

Font styles to use
Sans Serif

Requirements
Must have
• The package design must give the customer a WOW feeling. "HI-PROTEIN SNACK" must be highligted. Further, the design must use the Four Factors setup (attached).

```html
<!DOCTYPE html>
<html lang="en">
<head>
<meta charset="utf-8">
<title>fjordbite – Norwegian Salmon Snack Packaging</title>
<link href="https://fonts.googleapis.com/css2?family=Montserrat:wght@900&family=Ubuntu:wght@500;700&family=Amatic+SC:wght@700&display=swap" rel="stylesheet">
<style>
  :root {
    --backdrop: #ece8e2;
    --ink-dark: #1f2a2e;
    --white: #ffffff;
    --mango: #f7cf22;
    --mango-deep: #eab814;
    --mango-badge: #f0bd16;
    --mango-net: #e6d63a;
    --wasabi: #cfe03a;
    --wasabi-deep: #b9cd2a;
    --wasabi-badge: #a9cd3c;
    --wasabi-net: #e0d63a;
    --salmon-light: #f5a36e;
    --salmon-deep: #d8683a;
  }
  * { box-sizing: border-box; margin: 0; padding: 0; }
  html, body { width: 1200px; height: 857px; overflow: hidden; }
  body {
    background: var(--backdrop);
    font-family: "Ubuntu", sans-serif;
    position: relative;
  }
  .bag {
    position: absolute;
    top: 128px;
    width: 380px;
    height: 600px;
    background: var(--flavor);
    overflow: hidden;
    border-radius: 4px;
  }
  .bag--mango { left: 170px; --flavor: var(--mango); --flavor-deep: var(--mango-deep); --badge: var(--mango-badge); --net: var(--mango-net); }
  .bag--wasabi { left: 650px; --flavor: var(--wasabi); --flavor-deep: var(--wasabi-deep); --badge: var(--wasabi-badge); --net: var(--wasabi-net); }

  .top-band { position: absolute; top: 0; left: 0; width: 380px; height: 250px; }
  .crimp {
    position: absolute; left: 0; width: 100%; height: 20px;
    background: repeating-linear-gradient(180deg, rgba(0,0,0,0.12) 0 2px, transparent 2px 5px);
  }
  .crimp--top { top: 0; }
  .crimp--bottom { bottom: 0; background-color: var(--flavor-deep); }

  .brand {
    position: absolute; top: 92px; left: 0; width: 100%;
    display: flex; justify-content: center; align-items: center; gap: 8px;
    color: var(--white);
    font-family: "Ubuntu", sans-serif; font-weight: 700; font-size: 58px;
    letter-spacing: -1px;
  }
  .brand-dot { width: 12px; height: 12px; border-radius: 50%; background: var(--white); margin-top: -26px; }

  .claim-badge {
    position: absolute; top: 268px; left: 22px;
    width: 104px; height: 104px; border-radius: 50%;
    background: var(--badge);
    display: flex; flex-direction: column; align-items: center; justify-content: center;
    font-family: "Amatic SC", sans-serif; font-weight: 700;
    color: rgba(255,255,255,0.9); line-height: 1.05; text-align: center;
  }
  .claim-badge .claim-line { font-size: 12px; }
  .claim-badge .claim-rule { width: 74px; height: 1px; background: rgba(255,255,255,0.85); margin: 3px 0; }
  .claim-badge .claim-big { font-size: 20px; }

  .product-photo {
    position: absolute; top: 290px; left: 130px;
    width: 130px; height: 140px;
    border-radius: 45% 55% 50% 40%;
    background: radial-gradient(circle at 50% 45%, var(--salmon-light), var(--salmon-deep));
  }

  .flavor-name {
    position: absolute; top: 452px; left: 0; width: 100%; text-align: center;
    font-family: "Montserrat", sans-serif; font-weight: 900; font-size: 46px;
    color: var(--white); letter-spacing: 1px;
  }
  .flavor-sub {
    position: absolute; top: 508px; left: 0; width: 100%; text-align: center;
    font-family: "Ubuntu", sans-serif; font-weight: 500; font-size: 22px; color: var(--white);
  }
  .net-weight {
    position: absolute; top: 548px; left: 0; width: 100%; text-align: center;
    font-family: "Ubuntu", sans-serif; font-weight: 700; font-size: 13px; color: var(--net);
  }
  .origin-mark {
    position: absolute; top: 530px; left: 22px;
    width: 26px; height: 40px; border-radius: 3px;
    background: rgba(31,42,46,0.85);
  }
</style>
</head>
<body>

  <article class="bag bag--mango">
    <svg class="top-band" viewBox="0 0 380 250" aria-hidden="true">
      <path fill="var(--ink-dark)" d="M0,0 H380 V232 q-19,-16 -38,0 q-19,-16 -38,0 q-19,-16 -38,0 q-19,-16 -38,0 q-19,-16 -38,0 q-19,-16 -38,0 q-19,-16 -38,0 q-19,-16 -38,0 q-19,-16 -38,0 q-19,-16 -38,0 Z"/>
    </svg>
    <div class="crimp crimp--top"></div>
    <div class="brand">fjordbite<span class="brand-dot"></span></div>
    <div class="claim-badge">
      <span class="claim-line">LOW IN CARB (2%)</span>
      <span class="claim-line">HIGH IN PROTEIN (60%)</span>
      <span class="claim-rule"></span>
      <span class="claim-line">HIGH IN</span>
      <span class="claim-big">OMEGA 3</span>
    </div>
    <div class="product-photo" role="img" aria-label="Photo of dried salmon snack pieces"></div>
    <h2 class="flavor-name">MANGO</h2>
    <p class="flavor-sub">Norwegian Salmon</p>
    <p class="net-weight">Net WT 30g</p>
    <div class="origin-mark" aria-hidden="true"></div>
    <div class="crimp crimp--bottom"></div>
  </article>

  <article class="bag bag--wasabi">
    <svg class="top-band" viewBox="0 0 380 250" aria-hidden="true">
      <path fill="var(--ink-dark)" d="M0,0 H380 V232 q-19,-16 -38,0 q-19,-16 -38,0 q-19,-16 -38,0 q-19,-16 -38,0 q-19,-16 -38,0 q-19,-16 -38,0 q-19,-16 -38,0 q-19,-16 -38,0 q-19,-16 -38,0 q-19,-16 -38,0 Z"/>
    </svg>
    <div class="crimp crimp--top"></div>
    <div class="brand">fjordbite<span class="brand-dot"></span></div>
    <div class="claim-badge">
      <span class="claim-line">LOW IN CARB (2%)</span>
      <span class="claim-line">HIGH IN PROTEIN (60%)</span>
      <span class="claim-rule"></span>
      <span class="claim-line">HIGH IN</span>
      <span class="claim-big">OMEGA 3</span>
    </div>
    <div class="product-photo" role="img" aria-label="Photo of dried salmon snack pieces"></div>
    <h2 class="flavor-name">WASABI</h2>
    <p class="flavor-sub">Norwegian Salmon</p>
    <p class="net-weight">Net WT 30g</p>
    <div class="origin-mark" aria-hidden="true"></div>
    <div class="crimp crimp--bottom"></div>
  </article>

</body>
</html>
```